BrivoMatex. Lantern for the Steady Growth. Business card

Professional business card for BrivoMatex (Lantern for the Steady Growth)
My rationale: Strategy-> Execution-> Results-> Value that lead to the BrivoMatex name: We put the Lantern for the Steady Growth.
We deliver value to our customers helping them at defining a good strategy (cyan arrow). 90% of well formulated strategies fail due to poor execution so we also consider strategical execution very important (green arrow). Due to the execution we obtain the results (blue arrow). Finally, the results provide feedback to redefine strategy, and the new strategy has to be executed and new results obtained providing new feedback and on and on. It's like a wheel that finally, must create corporate value: value for shareholders, staholders, employees, providers...-

Target Market(s)

CEOs and steering comitees , invewrnent funds

Industry/Entity Type

Business Consultant

Contact Information for Business Card

Tommaso Ferlini
CEO & Founder
tommaso.ferlini@brivomatex.example
Mobile: +34 611.205.938
www.brivomatex.example

Colors

Designer to choose colors to be used in the design.

Requirements
Nice to have
• Nice to hace the words: Strategy, execution, results
• Nice to vave the claim: Lantern for the Steady Growth
• The three colors should be shown:
• cyan for STRATEGY
• green for EXECUTION
• blue for RESULTS
Should not have
• Complete black background

```html
<!DOCTYPE html>
<html lang="en">
<head>
<meta charset="utf-8">
<title>BrivoMatex — Business Card</title>
<link rel="stylesheet" href="https://fonts.googleapis.com/css2?family=Roboto:wght@400;700&display=swap">
<style>
  :root {
    --backdrop: #d6d7d9;
    --card-blue: #00359b;
    --card-edge: #7fc31c;
    --ink-white: #ffffff;
    --ink-soft: rgba(255, 255, 255, 0.88);
    --divider: rgba(255, 255, 255, 0.55);
  }
  * { margin: 0; padding: 0; box-sizing: border-box; }
  html, body {
    width: 1200px;
    height: 800px;
    overflow: hidden;
    background: var(--backdrop);
    font-family: "Roboto", Arial, sans-serif;
  }
  .canvas {
    width: 1200px;
    height: 800px;
    display: flex;
    align-items: center;
    justify-content: center;
    gap: 40px;
  }
  .card {
    width: 540px;
    height: 309px;
    background: var(--card-blue);
    border-bottom: 3px solid var(--card-edge);
    color: var(--ink-white);
    position: relative;
    box-shadow: 0 14px 28px rgba(0, 0, 0, 0.22);
  }

  /* Front */
  .card-front { display: flex; align-items: center; }
  .front-brand {
    width: 50%;
    display: flex;
    align-items: center;
    justify-content: center;
    gap: 10px;
  }
  .brand-dot {
    width: 14px;
    height: 14px;
    border-radius: 50%;
    background: var(--ink-white);
  }
  .brand-name {
    font-size: 34px;
    font-weight: 700;
    letter-spacing: -0.5px;
  }
  .front-divider {
    width: 1px;
    height: 110px;
    background: linear-gradient(to bottom, transparent, var(--divider), transparent);
  }
  .front-details { padding-left: 30px; }
  .person-name { font-size: 19px; font-weight: 700; }
  .person-role { font-size: 12px; color: var(--ink-soft); margin: 3px 0 14px; }
  .contact-list { list-style: none; font-size: 11.5px; color: var(--ink-soft); }
  .contact-list li { display: flex; align-items: center; gap: 8px; line-height: 19px; }
  .contact-list svg { width: 11px; height: 11px; flex: none; }

  /* Back */
  .card-back {
    display: flex;
    flex-direction: column;
    align-items: center;
    justify-content: center;
  }
  .back-brand { font-size: 58px; font-weight: 700; letter-spacing: -1px; margin-top: 10px; }
  .back-url {
    position: absolute;
    bottom: 52px;
    font-size: 12px;
    letter-spacing: 8px;
    color: var(--ink-soft);
  }
</style>
</head>
<body>
<main class="canvas">
  <section class="card card-front" aria-label="Business card front">
    <div class="front-brand">
      <span class="brand-dot"></span>
      <span class="brand-name">BrivoMatex</span>
    </div>
    <div class="front-divider"></div>
    <div class="front-details">
      <p class="person-name">Tommaso Ferlini</p>
      <p class="person-role">CEO &amp; Founder</p>
      <ul class="contact-list">
        <li>
          <svg viewBox="0 0 12 12" aria-hidden="true"><rect x="2.5" y="0.5" width="7" height="11" rx="1" fill="none" stroke="#fff"/><circle cx="6" cy="9.5" r="0.8" fill="#fff"/></svg>
          +34 611.205.938
        </li>
        <li>
          <svg viewBox="0 0 12 12" aria-hidden="true"><rect x="0.5" y="2" width="11" height="8" fill="#fff"/><path d="M0.5 2 L6 6.5 L11.5 2" fill="none" stroke="#00359b"/></svg>
          tommaso.ferlini@brivomatex.example
        </li>
        <li>
          <svg viewBox="0 0 12 12" aria-hidden="true"><circle cx="6" cy="6" r="5.5" fill="#fff"/><path d="M0.5 6 H11.5 M6 0.5 C3 3.5 3 8.5 6 11.5 M6 0.5 C9 3.5 9 8.5 6 11.5" fill="none" stroke="#00359b" stroke-width="0.8"/></svg>
          www.brivomatex.example
        </li>
      </ul>
    </div>
  </section>

  <section class="card card-back" aria-label="Business card back">
    <p class="back-brand">BrivoMatex</p>
    <p class="back-url">www.brivomatex.example</p>
  </section>
</main>
</body>
</html>
```